Do i have coronavirus, flue or cold?

Using information from QRV and government agencies we want to make a easy to read infographic helping patients see if they have coronavirus, the flu or a cold. Using a flow diagram or whatever you think will make it easy to read and digest for the average lamen.

Information is in the word document and in the chart.

We are www.tovipharm.co.uk attached is our brand guidelines, we will be putting this infographic on our website and email/sms it to all of our 300,000 patients.

```html
<!DOCTYPE html>
<html lang="en">
<head>
<meta charset="utf-8">
<title>Do You Have Symptoms of Corona Virus?</title>
<link href="https://fonts.googleapis.com/css2?family=Montserrat:wght@300;700;800;900&display=swap" rel="stylesheet">
<style>
  :root {
    --ink: #333333;
    --blue: #3434bb;
    --blue-light: #6b8cf0;
    --orange: #f55e20;
    --orange-light: #fca07f;
    --navy-text: #14143c;
    --cell-border: #6a6a6a;
    --paper: #ffffff;
  }
  * { margin: 0; padding: 0; box-sizing: border-box; }
  html, body { width: 1200px; height: 869px; overflow: hidden; background: var(--paper); }
  body { font-family: "Montserrat", Arial, sans-serif; position: relative; }

  .headline { position: absolute; left: 0; width: 1200px; text-align: center; color: var(--ink); white-space: nowrap; }
  .headline-lead { top: 47px; font-size: 56px; font-weight: 800; letter-spacing: 0.02em; line-height: 1; }
  .headline-main { top: 108px; font-size: 116px; font-weight: 900; letter-spacing: 0; line-height: 1; }

  .column { position: absolute; top: 245px; }
  .col-symptoms { left: 73px; width: 297px; }
  .col-covid { left: 416px; width: 200px; }
  .col-cold { left: 665px; width: 200px; }
  .col-flu { left: 910px; width: 200px; }

  .column-head {
    height: 84px; border: 4px solid var(--ink); border-radius: 16px;
    display: flex; align-items: center; justify-content: center;
    color: #fff; font-size: 32px; font-weight: 800; letter-spacing: 0.03em;
    white-space: nowrap;
    text-shadow: 2px 2px 3px rgba(0,0,0,0.45);
  }
  .head-blue { background: var(--blue); }
  .head-orange { background: var(--orange); }
  .col-covid .column-head { font-size: 30px; letter-spacing: 0.01em; }

  .rail {
    position: absolute; top: 98px; left: 5px; right: 5px; height: 452px;
    background: var(--ink); border-radius: 10px 10px 0 0;
  }
  .rail-foot {
    position: absolute; top: 556px; left: 5px; right: 5px; height: 20px;
    background: var(--ink); border-radius: 0 0 22px 22px;
  }
  .col-symptoms .rail-foot { left: 0; right: 7px; }

  .rows { position: absolute; left: 0; right: 0; display: flex; flex-direction: column; gap: 12.7px; }
  .col-symptoms .rows { top: 99px; right: 7px; }
  .values { top: 107px; }

  .label {
    height: 38px; background: var(--ink); border-radius: 4px;
    display: flex; align-items: center; justify-content: center;
    color: #fff; font-size: 18px; font-weight: 800; letter-spacing: 0.045em;
    white-space: nowrap;
    text-shadow: 1px 1px 2px rgba(0,0,0,0.6);
  }

  .cell {
    height: 38px; border: 2px solid var(--cell-border); border-radius: 3px;
    display: flex; align-items: center; justify-content: center;
    font-size: 16.5px; font-weight: 800; letter-spacing: 0.05em;
    white-space: nowrap;
  }
  .cell.strong-orange { background: var(--orange); color: #fff; text-shadow: 1px 1px 2px rgba(0,0,0,0.45); }
  .cell.soft-orange { background: var(--orange-light); color: var(--navy-text); }
  .cell.strong-blue { background: var(--blue); color: #fff; text-shadow: 1px 1px 2px rgba(0,0,0,0.45); }
  .cell.soft-blue { background: var(--blue-light); color: var(--navy-text); }
  .note { font-weight: 300; margin-left: 5px; letter-spacing: 0.04em; }
</style>
</head>
<body>
  <h1>
    <span class="headline headline-lead">DO YOU HAVE SYMPTOMS OF</span>
    <span class="headline headline-main">CORONA VIRUS?</span>
  </h1>

  <section class="column col-symptoms">
    <div class="column-head head-blue">SYMPTOMS</div>
    <div class="rows">
      <div class="label">FEVER</div>
      <div class="label">COUGH</div>
      <div class="label">TIREDNESS</div>
      <div class="label">SHORTNESS OF BREATH</div>
      <div class="label">MUSCLE ACHES</div>
      <div class="label">HEADSACHE</div>
      <div class="label">SORE THROAT</div>
      <div class="label">STUFFY OR RUNNY NOSE</div>
      <div class="label">SNEEZING</div>
    </div>
    <div class="rail-foot"></div>
  </section>

  <section class="column col-covid">
    <div class="column-head head-orange">COVID-19</div>
    <div class="rail"></div>
    <div class="rows values">
      <div class="cell strong-orange">YES</div>
      <div class="cell strong-orange">YES</div>
      <div class="cell strong-orange">YES</div>
      <div class="cell strong-orange">YES</div>
      <div class="cell strong-orange">YES</div>
      <div class="cell soft-orange">SOMETIMES</div>
      <div class="cell soft-orange">SOMETIMES</div>
      <div class="cell soft-orange">RARE</div>
      <div class="cell soft-orange">NO</div>
    </div>
    <div class="rail-foot"></div>
  </section>

  <section class="column col-cold">
    <div class="column-head head-blue">COLD</div>
    <div class="rail"></div>
    <div class="rows values">
      <div class="cell strong-blue">YES<span class="note">(HIGH)</span></div>
      <div class="cell strong-blue">YES</div>
      <div class="cell strong-blue">YES</div>
      <div class="cell strong-blue">YES</div>
      <div class="cell strong-blue">YES<span class="note">(OFTEN)</span></div>
      <div class="cell strong-blue">YES</div>
      <div class="cell soft-blue">SOMETIMES</div>
      <div class="cell soft-blue">SOMETIMES</div>
      <div class="cell soft-blue">SOMETIMES</div>
    </div>
    <div class="rail-foot"></div>
  </section>

  <section class="column col-flu">
    <div class="column-head head-blue">FLU</div>
    <div class="rail"></div>
    <div class="rows values">
      <div class="cell soft-blue">RARE</div>
      <div class="cell soft-blue">MODERATE</div>
      <div class="cell soft-blue">MILD</div>
      <div class="cell soft-blue">RARE</div>
      <div class="cell soft-blue">MODERATE</div>
      <div class="cell soft-blue">RARE</div>
      <div class="cell strong-blue">YES</div>
      <div class="cell strong-blue">YES</div>
      <div class="cell strong-blue">YES</div>
    </div>
    <div class="rail-foot"></div>
  </section>
</body>
</html>
```